PebbleNest Preschool Flyer

Must include children who are of various races and colors and be within the age group of 2-5 years. No infant photos. Must have bright colors including red, yellow, green, and blue. Must include the logo.

We are a preschool that teaches Mandarin and Spanish too children ages 2-5. We are located in Washington, DC.

Target Market(s)

Parents from different ethnic backgrounds who would appreciate world language curriculum for their parents.

Industry/Entity Type

Childcare

Font styles to use
Serif

Colors
f04a51
0455a3
9bcb3c
fbed22

Requirements
Must have
• Must include children who are of various races and colors and be within the age group of 2-5 years. No infant photos. Must have bright colors including red, yellow, green, and blue. Must include the logo.
Nice to have
Should not have
• Just all Caucasian or all Asian children or children who look younger than 2 years old or older than 4 years old.

```html
<!DOCTYPE html>
<html lang="en">
<head>
<meta charset="utf-8">
<title>PebbleNest Preschool Brochure</title>
<link rel="stylesheet" href="https://fonts.googleapis.com/css2?family=Tinos:wght@400;700&display=swap">
<style>
  :root {
    --paper: #ffffff;
    --ink: #111111;
    --blue-light: #1d78c8;
    --blue-deep: #0f4f9e;
    --ring-blue: #1a5fb0;
    --tagline-blue: #2a90d8;
    --orange-deep: #f26522;
    --orange: #f7941d;
    --yellow: #fbbf1a;
    --red: #cd2131;
    --green: #8cc63f;
    --brand-red: #d7262e;
    --fold: #9a9a9a;
    --photo-warm-a: #e9c9a8;
    --photo-warm-b: #b8d4c6;
    --photo-soft-a: #efe6dc;
    --photo-soft-b: #d9b48e;
  }
  * { margin: 0; padding: 0; box-sizing: border-box; }
  html, body { width: 1200px; height: 849px; overflow: hidden; background: var(--paper); }
  .brochure {
    position: relative;
    width: 1200px;
    height: 849px;
    overflow: hidden;
    background: var(--paper);
    font-family: "Tinos", "Times New Roman", serif;
  }
  .photo { position: absolute; }
  .photo--classroom {
    left: 0; top: 0; width: 404px; height: 414px;
    background: linear-gradient(135deg, var(--photo-warm-a) 0%, var(--photo-warm-b) 55%, #6aa6c9 100%);
  }
  .photo--friends {
    left: 671px; top: 0; width: 529px; height: 556px;
    background: linear-gradient(120deg, var(--photo-soft-a) 0%, var(--photo-soft-b) 50%, #9fcf7c 100%);
    clip-path: polygon(0 0, 529px 0, 529px 556px, 299px 556px);
  }
  .bands { position: absolute; left: 0; top: 0; width: 1200px; height: 849px; }
  .info-panel {
    position: absolute;
    left: 0; top: 414px; width: 404px; height: 435px;
    background: linear-gradient(180deg, var(--blue-light) 0%, var(--blue-deep) 100%);
    padding: 24px 46px 0 47px;
  }
  .info-panel__text {
    color: var(--paper);
    font-size: 15.5px;
    line-height: 19.8px;
    text-align: justify;
    hyphens: auto;
  }
  .fold {
    position: absolute; top: 0; width: 0; height: 849px;
    border-left: 1.5px dashed var(--fold);
  }
  .fold--first { left: 404px; }
  .fold--second { left: 806px; }
  .brand-name {
    color: var(--brand-red);
    font-weight: 400;
    text-align: center;
    line-height: 1.05;
  }
  .intro {
    position: absolute;
    left: 445px; top: 642px; width: 292px;
  }
  .intro .brand-name { font-size: 27px; width: 136px; margin-bottom: 22px; }
  .intro__text {
    color: var(--ink);
    font-size: 15px;
    line-height: 21px;
    text-align: justify;
  }
  .emblem {
    position: absolute;
    left: 935px; top: 328px; width: 314px; height: 314px;
    border-radius: 50%;
    background: var(--paper);
    border: 14px solid var(--ring-blue);
  }
  .emblem .brand-name {
    position: absolute; left: 0; top: 150px; width: 300px;
    padding-right: 14px;
    font-size: 30px;
  }
  .tagline {
    position: absolute;
    left: 1000px; top: 676px; width: 172px;
    color: var(--tagline-blue);
    font-size: 23px;
    line-height: 29px;
    text-align: right;
  }
</style>
</head>
<body>
<main class="brochure">
  <div class="photo photo--classroom" role="img" aria-label="Photo of smiling preschool children of different backgrounds sitting together on a classroom floor"></div>
  <div class="photo photo--friends" role="img" aria-label="Photo of three smiling preschool friends of different backgrounds standing close together"></div>

  <svg class="bands" viewBox="0 0 841 595" preserveAspectRatio="none" aria-hidden="true">
    <defs>
      <linearGradient id="lowerBandFill" x1="0" y1="0" x2="0" y2="1">
        <stop offset="0" stop-color="#f47b20"/>
        <stop offset="1" stop-color="#fcc216"/>
      </linearGradient>
      <linearGradient id="upperBandFill" x1="0" y1="0" x2="1" y2="1">
        <stop offset="0" stop-color="#f89a1c"/>
        <stop offset="1" stop-color="#fcc216"/>
      </linearGradient>
    </defs>
    <polygon points="680,390 740,390 650,595 585,595" fill="var(--green)"/>
    <polygon points="620,390 680,390 585,595 525,595" fill="var(--red)"/>
    <polygon points="490,390 620,390 525,595 395,595" fill="url(#lowerBandFill)"/>
    <polygon points="385,0 470,0 680,390 620,390" fill="url(#upperBandFill)"/>
    <polygon points="255,0 385,0 620,390 490,390" fill="var(--orange-deep)"/>
  </svg>

  <section class="info-panel">
    <p class="info-panel__text">Lorem ipsum dolor sit amet, consectetur adipiscing elit. Maecenas sagittis consequat mauris et sagittis. Cras et diam vulputate, bibendum sapien quis, aliquam diam. In hac habitasse platea dictumst. Duis posuere sed purus id suscipit. Sed varius ex id urna tempus pulvinar. Cras fringilla lorem eget augue dignissim mattis. Pellentesque habitant morbi tristique senectus et netus et malesuada fames ac turpis egestas. Duis auctor semper egestas. Duis sit amet ullamcorper dui, et dignissim risus. Quisque urna est, interdum non commodo non, hendrerit at quam. Pellentesque in ex euismod, interdum enim eu, sodales mi. Pellentesque ac sollicitudin dolor, lobortis consectetur eros.Lorem ipsum dolor sit amet, consectetur adipiscing elit. Maecenas sagittis consequat mauris et sagittis. Cras et diam vulputate, bibendum</p>
  </section>

  <div class="fold fold--first"></div>
  <div class="fold fold--second"></div>

  <section class="intro">
    <p class="brand-name">PebbleNest Preschool</p>
    <p class="intro__text">Lorem ipsum dolor sit amet, consectetur adipiscing elit. Maecenas sagittis consequat mauris et sagittis. Cras et diam vulputate, bibendum sapien quis, aliquam diam. In hac habitasse platea dictumst. Duis posuere sed</p>
  </section>

  <div class="emblem">
    <p class="brand-name">PebbleNest<br>Preschool</p>
  </div>

  <p class="tagline">Lorem ipsum dolor sit amet, consectetur adipiscing elit.</p>
</main>
</body>
</html>
```